Non fiction leadership Book Cover design needed for “Hold Fast: Forge A Steady Track”

I need a front cover design for a new book 6 X 9 traditional non-fiction book.

Title: "Hold FAST - Forge A Steady Track"

The subtitle is not finalized- so use 2 lines of smaller dummy text

My brand guide is attached (please use the tan color sparingly)

I'd like to see FAST look like it is in motion and "flying" across the page

Need CREATIVE designs and options

Do not want my picture on the front cover - I do want it on the back cover.

On the front cover I’d like to see creative use of font to create movement on “FAST”

Target Market(s)

Business leaders

Industry/Entity Type

Aviation

Font styles to use
Other font styles liked:
• See style guide- can add additional font (modern script or san serif)

Colors
0054AA
0677BA
7BADD7
CADEEF
E8F1F8
EB3D1F
EC4F4E
F09395
F8D3D4
FCEDEE

Requirements
Must have
• Creative font use, using perspective to create movement/motion on FAST
Should not have
• My picture on the front cover- my picture should be on the back cover

```html
<!DOCTYPE html>
<html lang="en">
<head>
<meta charset="utf-8">
<title>Hold Fast: Forge A Steady Track — Front Cover</title>
<link href="https://fonts.googleapis.com/css2?family=Bebas+Neue&family=Montserrat:wght@300;800;900&display=swap" rel="stylesheet">
<style>
  :root {
    --stage: #aaa8a9;
    --cover-ink: #0f1722;
    --cover-ink-soft: #1c2b40;
    --blue-deep: #0054aa;
    --blue-mid: #0677ba;
    --blue-light: #7badd7;
    --blue-pale: #cadeef;
    --red-strong: #eb3d1f;
    --red-soft: #ec4f4e;
    --red-pale: #f09395;
    --paper: #ffffff;
  }
  * { margin: 0; padding: 0; box-sizing: border-box; }
  html, body {
    width: 1200px;
    height: 1200px;
    overflow: hidden;
    background: var(--stage);
  }
  .stage {
    position: relative;
    width: 1200px;
    height: 1200px;
  }
  .book-cover {
    position: absolute;
    left: 238px;
    top: 58px;
    width: 723px;
    height: 1083px;
    display: block;
  }
  .author-name {
    font-family: "Montserrat", sans-serif;
    font-weight: 800;
    font-size: 27px;
    fill: var(--paper);
  }
  .title-main {
    font-family: "Montserrat", sans-serif;
    font-weight: 900;
    font-size: 262px;
  }
  .title-sub {
    font-family: "Bebas Neue", sans-serif;
    font-size: 98px;
    fill: var(--paper);
  }
  .tagline {
    font-family: "Montserrat", sans-serif;
    font-weight: 300;
    font-size: 23px;
    fill: var(--paper);
  }
  .speed-line {
    stroke-linecap: round;
  }
</style>
</head>
<body>
<main class="stage">
  <svg class="book-cover" viewBox="0 0 723 1083" xmlns="http://www.w3.org/2000/svg" aria-label="Hold Fast: Forge A Steady Track, by Margaret Hollister">
    <defs>
      <linearGradient id="title-blue" x1="0" y1="0" x2="0" y2="1">
        <stop offset="0" stop-color="var(--blue-light)"/>
        <stop offset="0.35" stop-color="var(--blue-mid)"/>
        <stop offset="1" stop-color="var(--blue-deep)"/>
      </linearGradient>
      <linearGradient id="title-red" x1="0" y1="0" x2="0" y2="1">
        <stop offset="0" stop-color="var(--red-pale)"/>
        <stop offset="0.35" stop-color="var(--red-soft)"/>
        <stop offset="1" stop-color="var(--red-strong)"/>
      </linearGradient>
      <linearGradient id="speed-fade" x1="0" y1="0" x2="1" y2="0">
        <stop offset="0" stop-color="var(--red-soft)" stop-opacity="0"/>
        <stop offset="1" stop-color="var(--red-soft)" stop-opacity="0.9"/>
      </linearGradient>
      <linearGradient id="base-band-fill" x1="0" y1="0" x2="1" y2="0">
        <stop offset="0" stop-color="var(--red-soft)"/>
        <stop offset="0.5" stop-color="var(--red-strong)"/>
        <stop offset="1" stop-color="var(--blue-deep)"/>
      </linearGradient>
      <linearGradient id="rule-fade" x1="0" y1="0" x2="1" y2="0">
        <stop offset="0" stop-color="var(--blue-light)" stop-opacity="0"/>
        <stop offset="0.5" stop-color="var(--blue-pale)"/>
        <stop offset="1" stop-color="var(--blue-light)" stop-opacity="0"/>
      </linearGradient>
      <radialGradient id="flight-glow" cx="0.8" cy="0.2" r="1">
        <stop offset="0" stop-color="var(--blue-deep)" stop-opacity="0.55"/>
        <stop offset="0.55" stop-color="var(--cover-ink-soft)"/>
        <stop offset="1" stop-color="var(--cover-ink)"/>
      </radialGradient>
    </defs>

    <rect class="cover-ground" width="723" height="1083" fill="var(--cover-ink)"/>

    <rect class="flight-illustration" role="img"
          aria-label="Illustration: a flock of white paper planes following a single red lead paper plane upward across a dark sky with sparkles"
          x="0" y="695" width="723" height="344" fill="url(#flight-glow)"/>

    <text class="author-name" x="361" y="53" text-anchor="middle">MARGARET HOLLISTER</text>

    <text class="title-main" x="24" y="279" fill="url(#title-blue)"
          textLength="669" lengthAdjust="spacingAndGlyphs">HOLD</text>

    <g class="fast-motion">
      <g class="speed-lines" stroke="url(#speed-fade)">
        <line class="speed-line" x1="8" y1="318" x2="118" y2="318" stroke-width="6"/>
        <line class="speed-line" x1="30" y1="352" x2="112" y2="352" stroke-width="4"/>
        <line class="speed-line" x1="0" y1="390" x2="100" y2="390" stroke-width="8"/>
        <line class="speed-line" x1="22" y1="428" x2="90" y2="428" stroke-width="4"/>
        <line class="speed-line" x1="6" y1="462" x2="80" y2="462" stroke-width="6"/>
      </g>
      <g transform="translate(128 481) skewX(-14)">
        <text class="title-main fast-trail" x="-44" y="0" fill="var(--red-strong)" opacity="0.12"
              textLength="540" lengthAdjust="spacingAndGlyphs">FAST</text>
        <text class="title-main fast-trail" x="-22" y="0" fill="var(--red-strong)" opacity="0.25"
              textLength="540" lengthAdjust="spacingAndGlyphs">FAST</text>
        <text class="title-main fast-word" x="0" y="0" fill="url(#title-red)"
              textLength="540" lengthAdjust="spacingAndGlyphs">FAST</text>
      </g>
    </g>

    <text class="title-sub" x="47" y="585"
          textLength="628" lengthAdjust="spacingAndGlyphs">FORGE A STEADY TRACK</text>

    <rect class="title-rule" x="171" y="602" width="384" height="1.2" fill="url(#rule-fade)"/>

    <text class="tagline" x="361" y="638" text-anchor="middle">LOREM IPSUM DOLOR SIT AMET,</text>
    <text class="tagline" x="361" y="671" text-anchor="middle">CONSECTETUR ADIPISCING ELIT, SED DO</text>

    <rect class="base-band" x="0" y="1039" width="723" height="44" fill="url(#base-band-fill)"/>
  </svg>
</main>
</body>
</html>
```